Broschüre für gemeinnütziges Unternehmen in den Bereichen Kunst, Kultur, Genuss und Heimatpflege
Guten Morgen Tilda am Mühlbach, lieben Dank für die schöne, flexible und rasche Arbeit! Top Kontakt! Habe den Erhalt der Daten eben bestätigt. Viele Grüße Harald Wolting
Zielgruppe
Wir kümmern uns als gemeinnützige GmbH in der Stadt Erlenbruch um alles, was mit Kunst, Kultur, Genuss und Heimatpflege zu tun hat. Dafür erstellen wir immer zum Jahresende (Ende Oktober, Anfang November) eine Broschüre mit unserem Programm für das Folgejahr. Unsere Zielgruppe sind Bürgerinnen und Bürger aus dem ganzen Kreisgebiet und darüber hinaus, Altersstruktur 30plus. Der neue Look der Broschüre sollte hochwertig und modern sein.
Aufgabenstellung
Die Broschüre hat eine Klammerheftung und wird ca. 64 Seiten umfassen.
Format: 14,8 x 14,8 cm
In der Anlage an diese Anfrage befinden sich Fotos von Musterseiten, wobei 'Titelseite' die aktuelle Titelseite zeigt, 'Foto 1' eine bisherige Innenseite zeigt, 'Seite 2' und 'Seite 3/4' zeigen Musterseiten, die verdeutlichen sollen, in welche Moderene und reduzierte Richtung es gehen soll. 'Foto Übersicht' zeigt eine chronologische Übersicht. Die Broschüre soll also einen moderneren Look bekommen, gerne auch mal mit einer Doppelseite. Die Musterseiten 2 und 3/4 sind allerdings aus einer Broschüre einer Nachbarkommune, unser Heft sollte sich also davon unterscheiden.
Wichtig sind immer pro Innenseite (oder Innen-Doppelseite): Ein Foto, Titel (z.B. 'Malvina', Genre 'Live-Musik' oder 'Musik und Songnächte', Eckdaten (Datum, Uhrzeit, Location, weitere Infos), Text.
Uns wäre mit einer schön gestalteten Titelseite, sowie schön gestalteten Muster-Innenseiten (je eine Einzelseite, eine Doppelseite, eine Seite mit tabellarischer Übersicht) sehr geholfen. Wir würden dann mit der Vorlage arbeiten und die anderen Seiten 'bauen'. Wäre das ein gangbarer Weg?
Für die Titelseite kann sehr gerne Stockmaterial verwendet werden, für den Innenteil stellen wir die Fotos.
Vielleicht können Musterseiten zu 'Malvina' ('Foto 1') gestaltet werden? Das passenden Foto hängt an, es kann mit Blindtext gearbeitet werden.
Ich freue mich über ein rasches Angebot.
Ihr
Harald Wolting

```html
<!DOCTYPE html>
<html lang="de">
<head>
<meta charset="utf-8">
<title>Ausblick 2024 – Programmübersicht</title>
<link href="https://fonts.googleapis.com/css2?family=Fira+Sans:ital,wght@0,400;0,500;0,600;1,300;1,400;1,600&display=swap" rel="stylesheet">
<style>
  :root {
    --teal: #1e8799;
    --white: #ffffff;
    --ink: #111111;
    --rule: #9a9a9a;
  }
  * { margin: 0; padding: 0; box-sizing: border-box; }
  html, body { width: 1200px; height: 600px; overflow: hidden; background: var(--white); }
  body { font-family: "Fira Sans", sans-serif; color: var(--ink); }
  .spread { position: relative; width: 1200px; height: 600px; display: flex; }

  .page { position: relative; width: 600px; height: 600px; }
  .page--intro { background: var(--teal); color: var(--white); }
  .page--program { background: var(--white); }

  .kicker {
    position: absolute; top: 42px; left: 40px;
    font-style: italic; font-weight: 400; font-size: 21px; letter-spacing: 0.3px;
  }
  .headline {
    position: absolute; top: 63px; left: 40px;
    font-weight: 600; font-size: 38px; letter-spacing: 2.2px; line-height: 1;
  }
  .page--program .kicker { left: 40px; color: var(--teal); }
  .page--program .headline { left: 40px; color: var(--ink); }

  .letter {
    position: absolute; top: 125px; left: 93px; width: 420px;
    font-style: italic; font-weight: 300; font-size: 12.9px; line-height: 17.2px;
  }
  .letter p + p { margin-top: 17.2px; }
  .letter strong { font-weight: 600; }

  .events { position: absolute; top: 124px; left: 93px; width: 414px; list-style: none; }
  .event {
    height: 43.6px; padding-top: 2px;
    border-bottom: 1px solid var(--rule);
  }
  .event + .event { padding-top: 4px; }
  .event__meta { font-weight: 500; font-size: 15px; line-height: 18px; letter-spacing: 0.2px; }
  .event__date { color: var(--teal); }
  .event__title { font-weight: 500; font-size: 13px; line-height: 17px; }

  .badge { position: absolute; left: 1013px; top: 420px; width: 64px; height: 64px; }
</style>
</head>
<body>
<main class="spread">
  <section class="page page--intro">
    <p class="kicker">ERLENBRUCH</p>
    <h1 class="headline">AUSBLICK 2024</h1>
    <div class="letter">
      <p>Liebe Kunst-, Kultur- und Genuss-Interessierte,</p>
      <p>non eum nusdame praerum quas magnatiasit, nimi, quid eostrum rene provid que liquam, apersperum veliqui buscienisqui velestota susae volorat autem <strong>inventiam autatiaest</strong> as con esequis eictor adipis volum ut es everro blabo. Arciae cus quos eos erro cone rerum et aut entius modis a volores moluptio. Nemporporem adipsaest estio tem quunt vent peliti aboreium harchil ium res dest, omnim que occat faceperum rehendae. Mus qui ate ligenihilis estrum, optur mos dis es endam, odia sed que nulpa cus.</p>
      <p>Natur? Ihit de dolum, ut es sunt ut qui dendi officiet plisquo cum facit atur, si id maiorrovitas et eum fugia doluptur, idero etur, vendigent latia perro eos as as doluptas int pero comnim essimperio. Et dem que nita quidebit des ima num net quam illabor eptions editibus susandus, sit expe coria quatem de perum re voluptate et <strong>prepernam cuptat</strong> mi, quatque netur am de voles vent.</p>
      <p>Non eum nusdame praerum quas magnatiasit, nimi, quid eostrum rene provid que liquam, apersperum veliqui buscienisqui velestota susae.</p>
      <p>Ihr Team der Kunst, Kultur und Heimatpflege Erlenbruch gGmbH.</p>
      <p>Harald Wolting, Petra Hoven und Nadine Krell</p>
    </div>
  </section>

  <section class="page page--program">
    <p class="kicker">MÄRZ | APRIL</p>
    <h2 class="headline">PROGRAMMÜBERSICHT</h2>
    <ul class="events">
      <li class="event"><p class="event__meta"><span class="event__date">SA 00. JANUAR</span> | 00 UHR | MUSTERPLATZ</p><p class="event__title">Malvina live Blindtext</p></li>
      <li class="event"><p class="event__meta"><span class="event__date">SA 00. JANUAR</span> | 00 UHR | MUSTERPLATZ</p><p class="event__title">Malvina live Blindtext</p></li>
      <li class="event"><p class="event__meta"><span class="event__date">SA 00. JANUAR</span> | 00 UHR | MUSTERPLATZ</p><p class="event__title">Malvina live Blindtext</p></li>
      <li class="event"><p class="event__meta"><span class="event__date">SA 00. JANUAR</span> | 00 UHR | MUSTERPLATZ</p><p class="event__title">Malvina live Blindtext</p></li>
      <li class="event"><p class="event__meta"><span class="event__date">SA 00. JANUAR</span> | 00 UHR | MUSTERPLATZ</p><p class="event__title">Malvina live Blindtext</p></li>
      <li class="event"><p class="event__meta"><span class="event__date">SA 00. JANUAR</span> | 00 UHR | MUSTERPLATZ</p><p class="event__title">Malvina live Blindtext</p></li>
      <li class="event"><p class="event__meta"><span class="event__date">SA 00. JANUAR</span> | 00 UHR | MUSTERPLATZ</p><p class="event__title">Malvina live Blindtext</p></li>
      <li class="event"><p class="event__meta"><span class="event__date">SA 00. JANUAR</span> | 00 UHR | MUSTERPLATZ</p><p class="event__title">Malvina live Blindtext</p></li>
      <li class="event"><p class="event__meta"><span class="event__date">SA 00. JANUAR</span> | 00 UHR | MUSTERPLATZ</p><p class="event__title">Malvina live Blindtext</p></li>
      <li class="event"><p class="event__meta"><span class="event__date">SA 00. JANUAR</span> | 00 UHR | MUSTERPLATZ</p><p class="event__title">Malvina live Blindtext</p></li>
    </ul>
  </section>

  <svg class="badge" viewBox="0 0 64 64" aria-label="Eintritt frei">
    <circle cx="32" cy="32" r="32" fill="var(--teal)"/>
    <text x="32" y="26" text-anchor="middle" fill="#fff" font-family="Fira Sans, sans-serif" font-weight="600" font-size="10.5" letter-spacing="0.3">EINTRITT</text>
    <text x="32" y="46" text-anchor="middle" fill="#fff" font-family="Fira Sans, sans-serif" font-weight="600" font-size="22" letter-spacing="0.5">FREI</text>
  </svg>
</main>
</body>
</html>
```